Brennor Electronics, Inc. Business card

Incorporate a globe.
We repair electronics, sell electronic parts, and we recycle electronics. We've been in business since 1982. A technology feel to the card is preferred. I want to be able to give this card to a client from different industries and make it relate-able. I don't have a logo that I've been partial to in the past. It is not necessary in this case.

Target Market(s)

Consumer, Industrial, Business, Medical

Industry/Entity Type

Business

Contact Information for Business Card

5184 Mulvane Blvd. Dallas, TX 75319
214-508-3764 main 214-508-3719 fax
Gavin Tresaldo VP

Font styles to use
Serif

Requirements
Must have
• Technology feel
Nice to have
• Metallic look
Should not have
• no pastel colors

```html
<!DOCTYPE html>
<html lang="en">
<head>
<meta charset="utf-8">
<title>Brennor Electronics, Inc. – Business Card</title>
<link rel="stylesheet" href="https://fonts.googleapis.com/css2?family=Open+Sans:wght@400;600&display=swap">
<style>
  :root {
    --canvas-bg: #e2e2e4;
    --card-white: #ffffff;
    --brand-blue: #1f8fc8;
    --brand-blue-light: #2aa6e0;
    --ink: #2b2b2b;
    --rule: #c9c9c9;
    --steel-dark: #5a5a5c;
    --steel-light: #a3a3a5;
    --back-dark: #2f2f30;
    --back-mid: #4c4c4d;
    --back-light: #747475;
    --logo-white: #ffffff;
  }
  * { box-sizing: border-box; margin: 0; padding: 0; }
  html, body {
    width: 1200px; height: 1000px; overflow: hidden;
    background: var(--canvas-bg);
    font-family: "Open Sans", Arial, sans-serif;
    color: var(--ink);
  }
  .canvas { position: relative; width: 1200px; height: 1000px; }

  .card { position: absolute; left: 265px; width: 666px; height: 397px; overflow: hidden; }
  .card--front { top: 73px; background: var(--card-white); }
  .card--back {
    top: 532px;
    background: radial-gradient(circle at 18% 22%, var(--back-light) 0%, var(--back-mid) 38%, var(--back-dark) 80%);
  }

  .brand { position: absolute; display: flex; align-items: center; gap: 16px; }
  .brand__dot { width: 64px; height: 64px; border-radius: 50%; flex: none; }
  .brand__name {
    font-weight: 600; font-size: 29px; line-height: 1.08;
    letter-spacing: 1.5px; text-transform: uppercase;
  }
  .card--front .brand { right: 33px; top: 72px; }
  .card--front .brand__dot { background: var(--brand-blue); }
  .card--front .brand__name { color: var(--brand-blue); }
  .card--back .brand { right: 32px; top: 288px; }
  .card--back .brand__dot { background: var(--logo-white); }
  .card--back .brand__name { color: var(--logo-white); }

  .person { position: absolute; left: 33px; top: 206px; }
  .person__name { font-weight: 600; font-size: 22px; color: var(--brand-blue); letter-spacing: .3px; }
  .person__title { font-size: 16px; margin-top: 2px; }

  .divider { position: absolute; left: 33px; top: 267px; width: 452px; height: 1px; background: var(--rule); }

  .address { position: absolute; left: 33px; top: 293px; font-size: 16px; line-height: 21px; }

  .contact { position: absolute; right: 30px; top: 256px; list-style: none; font-size: 16px; }
  .contact__item { display: flex; justify-content: flex-end; align-items: center; gap: 7px; height: 24.5px; }
  .contact__icon { width: 16px; height: 16px; flex: none; }

  .bands { position: absolute; left: 0; bottom: 0; width: 666px; height: 28px; }
</style>
</head>
<body>
<main class="canvas">

  <section class="card card--front" aria-label="Business card front">
    <div class="brand">
      <span class="brand__dot"></span>
      <span class="brand__name">Brennor<br>Electronics</span>
    </div>

    <div class="person">
      <p class="person__name">GAVIN TRESALDO</p>
      <p class="person__title">Vice President</p>
    </div>

    <div class="divider"></div>

    <address class="address" style="font-style:normal">
      Suite 12, 5184 Mulvane Blvd.<br>
      Dallas, TX 75319
    </address>

    <ul class="contact">
      <li class="contact__item">+ 000 000 0000
        <svg class="contact__icon" viewBox="0 0 16 16" aria-hidden="true">
          <rect x="4.5" y="1" width="7" height="14" rx="1.2" fill="none" stroke="#1f8fc8" stroke-width="1.4"/>
          <rect x="6" y="3" width="4" height="4" fill="#1f8fc8"/>
        </svg>
      </li>
      <li class="contact__item">+ 000 000 0000
        <svg class="contact__icon" viewBox="0 0 16 16" aria-hidden="true">
          <path d="M2 6c0-2 2-3 6-3s6 1 6 3l-3 1-1-2H6L5 7z" fill="#1f8fc8"/>
          <path d="M4 8h8l1 5H3z" fill="#1f8fc8"/>
        </svg>
      </li>
      <li class="contact__item">info@brennorelectronics.com
        <svg class="contact__icon" viewBox="0 0 16 16" aria-hidden="true">
          <rect x="1.5" y="3.5" width="13" height="9" fill="#1f8fc8"/>
          <path d="M1.5 3.5 8 9l6.5-5.5" fill="none" stroke="#fff" stroke-width="1.2"/>
        </svg>
      </li>
      <li class="contact__item">www.brennorelectronics.com
        <svg class="contact__icon" viewBox="0 0 16 16" aria-hidden="true">
          <circle cx="8" cy="8" r="6.3" fill="none" stroke="#1f8fc8" stroke-width="1.5"/>
          <path d="M1.7 8h12.6M8 1.7v12.6" stroke="#1f8fc8" stroke-width="1.2"/>
        </svg>
      </li>
    </ul>

    <svg class="bands" viewBox="0 0 666 28" aria-hidden="true">
      <defs>
        <linearGradient id="bandBlue" x1="0" x2="1">
          <stop offset="0" stop-color="#1a76a8"/>
          <stop offset="1" stop-color="#2aa6e0"/>
        </linearGradient>
        <linearGradient id="bandSteel" x1="0" x2="1">
          <stop offset="0" stop-color="#a3a3a5"/>
          <stop offset="1" stop-color="#5a5a5c"/>
        </linearGradient>
      </defs>
      <polygon points="0,10 338,10 320,28 0,28" fill="url(#bandBlue)"/>
      <polygon points="357,0 666,0 666,28 330,28" fill="url(#bandSteel)"/>
    </svg>
  </section>

  <section class="card card--back" aria-label="Business card back">
    <div class="brand">
      <span class="brand__dot"></span>
      <span class="brand__name">Brennor<br>Electronics</span>
    </div>
  </section>

</main>
</body>
</html>
```